Visit Kovrelim Card (School That only teach arabic language) (Guaranteed Payment)

Hi, we are a new school That Teach arabic language in Tunisia, we are looking to conceptulize visit cards for our team. The business card will be printed in color and on Both Sides. We want to communiquer: innovation, excellence, professionalism, leadership and trust. Would we need the business card at the end with the details of everyone of our team (3) General and aussi has one for our center in Tunis. La même designed is used througout of course. Waiting for your sugestions! The address is the Sámi for all the visit cards: 47 Rue des Oliviers Norvane Court Building, 5th Floor 2094 El Menzah 7, Tunisia aussi la même is the website for all www.kovrelim.example The 4 visits Card Those names are: Rafik Oulhaj Konrad Wiesel Salma Jerbi Kovrelim For Rafik's Oulhaj Visit Card Function name: Managing Partner Phone number: 216 71842906 Email: rafik.oulhaj@kovrelim. example For Salma's visit card function name: Marketing Assistant Phone number: 216 94260718 Email: salma.jerbi@kovrelim.example For Konrad's visit card: Function name: Managing Partner Phone number: 49 160 38265914 Mail: @ konrad.wiesel kovrelim.example You can find our logo in the attachment.

```html
<!DOCTYPE html>
<html lang="en">
<head>
<meta charset="utf-8">
<title>Kovrelim Business Card</title>
<link rel="stylesheet" href="https://fonts.googleapis.com/css2?family=Source+Sans+3:wght@400;600;700&display=swap">
<style>
  :root {
    --page-bg: #e9e7e4;
    --card-white: #fbfbfa;
    --card-black: #151515;
    --brand-blue: #0d4e8f;
    --text-dark: #2a2a2a;
    --text-mid: #4a4a4a;
    --text-light: #ffffff;
  }
  * { margin: 0; padding: 0; box-sizing: border-box; }
  html, body {
    width: 1200px;
    height: 844px;
    overflow: hidden;
    background: var(--page-bg);
    font-family: "Source Sans 3", "Myriad Pro", Arial, sans-serif;
  }
  .canvas {
    position: relative;
    width: 1200px;
    height: 844px;
  }
  .card {
    position: absolute;
    top: 267px;
    width: 540px;
    height: 310px;
    box-shadow: 0 6px 18px rgba(0,0,0,0.18);
  }

  /* Front */
  .card-front {
    left: 40px;
    background: var(--card-white);
    color: var(--text-dark);
  }
  .front-logo {
    position: absolute;
    right: 34px;
    top: 34px;
    display: flex;
    align-items: center;
    gap: 10px;
    font-size: 44px;
    font-weight: 600;
    letter-spacing: 0.5px;
    color: var(--brand-blue);
    line-height: 1;
  }
  .logo-square {
    width: 16px;
    height: 16px;
    background: var(--brand-blue);
  }
  .rule {
    position: absolute;
    left: 0;
    right: 0;
    height: 1.5px;
    background: var(--brand-blue);
  }
  .rule-top { top: 100px; }
  .rule-mid { top: 183px; }
  .person {
    position: absolute;
    left: 30px;
    top: 128px;
  }
  .person-name {
    font-size: 21px;
    font-weight: 700;
    color: var(--brand-blue);
    line-height: 1.1;
  }
  .person-title {
    font-size: 14.5px;
    color: var(--text-mid);
    margin-top: 2px;
  }
  .contact {
    position: absolute;
    left: 30px;
    right: 24px;
    top: 200px;
    font-size: 14.5px;
    line-height: 1.6;
    color: var(--text-dark);
  }
  .contact .sep { margin: 0 6px; }
  .contact .web { color: var(--brand-blue); }
  .contact-line { white-space: nowrap; }

  /* Back */
  .card-back {
    left: 620px;
    background: var(--card-black);
    color: var(--text-light);
  }
  .back-logo {
    position: absolute;
    left: 0;
    right: 0;
    top: 112px;
    display: flex;
    justify-content: center;
    align-items: center;
    gap: 12px;
    font-size: 50px;
    font-weight: 600;
    letter-spacing: 0.5px;
    line-height: 1;
  }
  .back-logo .logo-square { background: var(--text-light); width: 18px; height: 18px; }
  .back-web {
    position: absolute;
    left: 0;
    right: 0;
    top: 200px;
    text-align: center;
    font-size: 12px;
    letter-spacing: 0.3px;
  }
</style>
</head>
<body>
<main class="canvas">
  <section class="card card-front" aria-label="Business card front">
    <div class="front-logo"><span class="logo-square"></span><span>kovrelim</span></div>
    <div class="rule rule-top"></div>
    <div class="person">
      <p class="person-name">Rafik's Oulhaj</p>
      <p class="person-title">Managing Partner</p>
    </div>
    <div class="rule rule-mid"></div>
    <div class="contact">
      <p class="contact-line">47 Rue des Oliviers Norvane Court Building, 5th Floor 2094 El</p>
      <p class="contact-line">Menzah 7, Tunisia</p>
      <p class="contact-line">216 71842906<span class="sep">|</span>rafik.oulhaj@kovrelim. example<span class="sep">|</span><span class="web">www.kovrelim.example</span></p>
    </div>
  </section>

  <section class="card card-back" aria-label="Business card back">
    <div class="back-logo"><span class="logo-square"></span><span>kovrelim</span></div>
    <p class="back-web">www.kovrelim.example</p>
  </section>
</main>
</body>
</html>
```